QMRLS Business Card Revamp: Professional and Modern Design for Enhanced Networking

The Northfield Animal Care Practitioners Guild (QMRLS) is seeking a redesign of its current business cards to better represent its professional image and improve its networking capabilities. The QMRLS is a professional association for veterinary technologists in Alberta, Canada, and it aims to promote the welfare of animals and the veterinary profession through continuing education, advocacy, and professional development.

The project objectives are to create a professional and modern design for the QMRLS business cards that accurately reflects the organization's values and mission. We would like to include our brand colors in the final design and make it editable to update different roles and positions for the association. The card will need to include the name, pronouns (if applicable), and position of the individual as well as an email address, phone, and website.

The final deliverables for this project will include a design concept for the new QMRLS business cards, a layout for the business cards that includes all relevant contact information and branding elements, and final design files in an editable format.

Target Market(s)

Members, industry stakeholders, government

Industry/Entity Type

Veterinary

Contact Information for Business Card

Name, pronouns (if applicable), title, logo, website, email, phone number

Font styles to use
Other font styles liked:
• Open Sans, logo font is Politica

Requirements
Must have
• Brand recognition, logo, professional and modern design
Nice to have
• double-sided - open to single sided
Should not have
• pictures of animals, hearts

```html
<!DOCTYPE html>
<html lang="en">
<head>
<meta charset="utf-8">
<title>QMRLS Business Card</title>
<link rel="stylesheet" href="https://fonts.googleapis.com/css2?family=Open+Sans:wght@400;600;700&display=swap">
<style>
  :root {
    --stage: #e6e6e6;
    --card-white: #ffffff;
    --card-dark: #2f2f2f;
    --card-dark-edge: #262626;
    --ink: #4f5b5d;
    --ink-soft: #6d6d6d;
    --accent-blue: #4ba8c9;
    --accent-green: #7cae43;
    --divider: #9a9a9a;
    --white: #ffffff;
  }
  * { box-sizing: border-box; margin: 0; padding: 0; }
  html, body {
    width: 1200px; height: 802px; overflow: hidden;
    background: var(--stage);
    font-family: "Open Sans", Arial, sans-serif;
  }
  .stage {
    position: relative; width: 1200px; height: 802px;
    display: flex; align-items: center; justify-content: center; gap: 50px;
  }
  .card {
    position: relative; width: 525px; height: 300px;
    box-shadow: 0 8px 22px rgba(0,0,0,0.18);
  }
  /* Front */
  .card--front { background: var(--card-white); }
  .brand {
    position: absolute; left: 44px; top: 62px; width: 210px;
    display: flex; align-items: center; gap: 10px;
  }
  .brand__dot { width: 14px; height: 14px; border-radius: 50%; background: var(--accent-green); flex: none; }
  .brand__name { font-size: 46px; font-weight: 700; color: var(--ink); letter-spacing: 1px; line-height: 1; }
  .brand__full {
    position: absolute; left: 44px; top: 118px; width: 230px;
    font-size: 9px; color: var(--ink); letter-spacing: 0.2px;
  }
  .divider {
    position: absolute; left: 282px; top: 58px; width: 1px; height: 84px;
    background: var(--divider);
  }
  .contacts { position: absolute; left: 302px; top: 60px; list-style: none; }
  .contacts li {
    display: flex; align-items: center; gap: 9px;
    font-size: 15px; color: var(--ink-soft); line-height: 26px;
  }
  .contacts svg { width: 13px; height: 13px; fill: var(--accent-blue); flex: none; }
  .person { position: absolute; left: 44px; top: 190px; }
  .person__name { font-size: 22px; font-weight: 600; color: var(--accent-blue); }
  .person__role { font-size: 16px; color: var(--ink-soft); margin-top: 2px; }
  .tagline {
    position: absolute; left: 302px; top: 200px;
    font-size: 15px; color: var(--ink-soft); letter-spacing: 0.3px;
  }
  .tagline b { color: var(--accent-blue); font-weight: 700; margin: 0 4px; }
  /* Back */
  .card--back {
    background: linear-gradient(160deg, var(--card-dark) 0%, var(--card-dark-edge) 100%);
  }
  .back-brand { position: absolute; right: 32px; top: 44px; text-align: right; }
  .back-brand__name {
    font-size: 76px; font-weight: 700; color: var(--white);
    letter-spacing: 2px; line-height: 1;
  }
  .back-brand__full { font-size: 12px; color: var(--white); margin-top: 4px; }
</style>
</head>
<body>
<main class="stage">
  <section class="card card--front" aria-label="Card front">
    <div class="brand">
      <span class="brand__dot"></span>
      <span class="brand__name">QMRLS</span>
    </div>
    <p class="brand__full">Northfield Animal Care Practitioners Guild</p>
    <span class="divider"></span>
    <ul class="contacts">
      <li>
        <svg viewBox="0 0 16 16" aria-hidden="true"><path d="M3.5 1l2.5 3-1.5 1.8c.9 2 2.7 3.8 4.7 4.7L11 9l3 2.5-1.4 2.8C7 14 2 9 1.7 3.4z"/></svg>
        555-014-2298
      </li>
      <li>
        <svg viewBox="0 0 16 16" aria-hidden="true"><path d="M1 3h14v10H1z M1 3l7 6 7-6" fill="none" stroke="#4ba8c9" stroke-width="1.6"/></svg>
        info@qmrls.org
      </li>
      <li>
        <svg viewBox="0 0 16 16" aria-hidden="true"><circle cx="8" cy="8" r="7"/><path d="M1 8h14M8 1c3 3 3 11 0 14M8 1c-3 3-3 11 0 14" fill="none" stroke="#fff" stroke-width="1"/></svg>
        www.qmrls.org
      </li>
    </ul>
    <div class="person">
      <p class="person__name">Dana Whitlock, RVT</p>
      <p class="person__role">Executive Director</p>
    </div>
    <p class="tagline"><b>•</b>Inform<b>•</b>Inspire<b>•</b>Connect</p>
  </section>

  <section class="card card--back" aria-label="Card back">
    <div class="back-brand">
      <p class="back-brand__name">QMRLS</p>
      <p class="back-brand__full">Northfield Animal Care Practitioners Guild</p>
    </div>
  </section>
</main>
</body>
</html>
```